Tolvane Handyman Service

File 2 Prep kitchen cabinets
File 3 Painting kitchen cabinets
File 4 Demo stairs
File 5 Completion Installing stair treads
File 6 Power washing deck
File 7 Completion of Sainting deck and railings
File 8 Completion of staining steps
Logo, owner name, email and web site on front cover
File 9 Demo living room floor
File 10 Completion of living room floor
Please see additional on attached flyer

Target Market(s)

Residential

Industry/Entity Type

Painting

Font styles to use
Serif
Sans Serif

Requirements
Must have
• Some Photos and type of work discerption
Front page Logo, web address, phone number, owners name and email address
Back Page see attached file 1
Nice to have
• Photo maybe in middle of flyer
Use the best text that you think will meet the needs
Should not have
• No pink colors

```html
<!DOCTYPE html>
<html lang="en">
<head>
<meta charset="utf-8">
<title>Tolvane Handyman Service – Tri-fold Brochure</title>
<link rel="stylesheet" href="https://fonts.googleapis.com/css2?family=Oswald:wght@400;500&family=Source+Sans+3:wght@400;600;700&display=swap">
<style>
:root{
  --page:#e6e7ea;
  --paper:#ffffff;
  --navy:#2a2e42;
  --navy-light:#444b63;
  --blue:#5a66b8;
  --blue-soft:#7f89c8;
  --ink:#1e2030;
  --grey-text:#3a3c48;
}
*{margin:0;padding:0;box-sizing:border-box}
html,body{width:792px;height:1200px;overflow:hidden}
body{background:var(--page);font-family:"Source Sans 3",Arial,sans-serif;color:var(--ink);position:relative}
.sheet{position:absolute;width:655px;height:509px;background:var(--paper);overflow:hidden}
.sheet--outside{left:70px;top:66px}
.sheet--inside{left:72px;top:629px}
.panel{position:absolute;top:0;height:100%}
.photo{position:absolute}
.dark{background:linear-gradient(180deg,var(--navy) 0%,var(--navy-light) 55%,var(--navy) 100%)}

/* footer web bar */
.web-bar{position:absolute;height:13px;background:var(--blue);color:#fff;font-size:7.5px;font-weight:600;letter-spacing:.4px;display:flex;align-items:center;gap:4px}
.web-bar svg{width:8px;height:8px}
.web-bar--left{left:0;width:168px;clip-path:polygon(0 0,100% 0,97% 100%,0 100%);padding-left:18px}
.web-bar--right{right:0;width:168px;clip-path:polygon(3% 0,100% 0,100% 100%,0 100%);padding-left:24px}

/* brand */
.brand{position:absolute;left:0;right:0;text-align:center}
.brand__mark{display:block;margin:0 auto 6px;background:var(--blue)}
.brand__name{font-weight:700;font-size:7.5px;color:#fff}
.brand__tag{font-weight:700;font-size:7px;color:var(--blue-soft)}
.brand--light .brand__name{color:var(--ink);font-size:10.5px}
.brand--light .brand__tag{color:var(--blue);font-size:10px}

/* outside left */
.about__circles{position:absolute;top:242px;left:0;width:100%}
.circle{position:absolute;width:66px;height:66px;border-radius:50%;border:3px solid var(--blue)}
.section-title{font-family:"Oswald",sans-serif;color:var(--blue);font-weight:400}
.about__title{position:absolute;left:19px;top:318px;font-size:15px}
.about__list{position:absolute;left:17px;top:354px;list-style:none;font-size:8.6px}
.about__list li{height:16px;display:flex;align-items:center;gap:5px}
.about__list svg{width:8px;height:8px}
.about__slogan{position:absolute;left:0;width:100%;top:448px;text-align:center;font-size:23px;letter-spacing:-.2px}

/* outside middle */
.tagline{position:absolute;top:141px;width:100%;text-align:center;color:#fff;font-size:16.5px;letter-spacing:2px;line-height:27px;font-weight:400}
.contact-tab{position:absolute;left:35px;top:269px;width:149px;height:20px;background:var(--blue);clip-path:polygon(3% 0,100% 0,97% 100%,0 100%);color:#fff;font-family:"Oswald",sans-serif;font-size:13px;text-align:center;line-height:20px}
.contact{position:absolute;top:301px;width:100%;text-align:center;color:#fff;font-style:normal}
.contact__company{font-size:12px;font-weight:600;line-height:16px}
.contact__owner{font-size:9.5px;font-weight:700;line-height:16px;margin-bottom:4px}
.contact__line{font-size:8.5px;line-height:19.5px}
.social{position:absolute;top:422px;width:100%;display:flex;justify-content:center;gap:7px}
.social span{width:11px;height:11px;border:1px solid #fff;border-radius:50%}
.web-box{position:absolute;left:17px;top:445px;width:182px;height:22px;border:1.5px solid #c9cce0;color:#fff;font-size:10.5px;font-weight:600;letter-spacing:1.3px;text-align:center;line-height:19px}

/* outside right */
.solution{position:absolute;top:431px;width:100%;text-align:center;font-family:"Oswald",sans-serif;font-size:22px;line-height:28px;color:#111;font-weight:400}

/* inside */
.side-bar{position:absolute;left:0;top:176px;width:15px;height:333px;background:var(--blue)}
.services__title{position:absolute;left:24px;top:189px;font-size:22px;letter-spacing:-.3px}
.services__text{position:absolute;left:27px;top:221px;width:187px;font-size:7.4px;line-height:9.65px;text-align:justify;color:var(--grey-text)}
.service{position:absolute}
.service__head{position:relative;height:22px}
.service__tab{position:absolute;left:0;top:0;height:22px;width:132px;background:var(--blue);clip-path:polygon(0 0,88% 0,100% 100%,0 100%);color:#fff;font-weight:700;font-size:13px;line-height:22px;padding-left:5px}
.service__rule{position:absolute;left:0;bottom:0;height:1px;background:var(--blue)}
.service__list{list-style:none;margin-top:9px;font-size:8.7px}
.service__list li{height:13.1px;display:flex;align-items:center;gap:6px}
.service__list li::before{content:"";width:4px;height:4px;background:var(--blue);flex:none}
.dark .service__list{color:#fff}
.tight{letter-spacing:-.35px}
</style>
</head>
<body>

<!-- Outside of brochure -->
<section class="sheet sheet--outside">

  <div class="panel" style="left:0;width:221px">
    <div class="photo" role="img" aria-label="Freshly stained deck steps with white risers and railing" style="left:0;top:0;width:221px;height:218px;background:linear-gradient(160deg,#d9dbe0 0%,#8c7a6a 45%,#5b4636 70%,#e8e8e8 100%)"></div>
    <div style="position:absolute;left:0;top:218px;width:221px;height:14px;background:var(--blue)"></div>
    <div class="about__circles">
      <div class="circle" role="img" aria-label="Painted kitchen cabinets" style="left:8px;background:radial-gradient(circle,#e9e6df,#a7998a)"></div>
      <div class="circle" role="img" aria-label="New living room floor" style="left:79px;background:radial-gradient(circle,#c9a070,#6c4e33)"></div>
      <div class="circle" role="img" aria-label="Completed stair treads" style="left:149px;background:radial-gradient(circle,#d7a36a,#8b5a2f)"></div>
    </div>
    <h2 class="section-title about__title">ABOUT US</h2>
    <ul class="about__list">
      <li><svg viewBox="0 0 10 10"><circle cx="5" cy="5" r="4.3" fill="none" stroke="#5a66b8"/><path d="M4 3l2 2-2 2" fill="none" stroke="#5a66b8"/></svg>35 years Experience</li>
      <li><svg viewBox="0 0 10 10"><circle cx="5" cy="5" r="4.3" fill="none" stroke="#5a66b8"/><path d="M4 3l2 2-2 2" fill="none" stroke="#5a66b8"/></svg>Free Written Estimates</li>
      <li><svg viewBox="0 0 10 10"><circle cx="5" cy="5" r="4.3" fill="none" stroke="#5a66b8"/><path d="M4 3l2 2-2 2" fill="none" stroke="#5a66b8"/></svg>Fully Insured</li>
      <li><svg viewBox="0 0 10 10"><circle cx="5" cy="5" r="4.3" fill="none" stroke="#5a66b8"/><path d="M4 3l2 2-2 2" fill="none" stroke="#5a66b8"/></svg>Locally Owned</li>
      <li><svg viewBox="0 0 10 10"><circle cx="5" cy="5" r="4.3" fill="none" stroke="#5a66b8"/><path d="M4 3l2 2-2 2" fill="none" stroke="#5a66b8"/></svg>Prompt Response</li>
    </ul>
    <p class="section-title about__slogan">ONE CALL DOES IT ALL</p>
    <div class="web-bar web-bar--left" style="top:488px"><svg viewBox="0 0 10 10"><circle cx="5" cy="5" r="4" fill="none" stroke="#fff"/><path d="M1 5h8M5 1v8" stroke="#fff" stroke-width=".8"/></svg>www.tolvanehandyman.com</div>
  </div>

  <div class="panel dark" style="left:221px;width:216px">
    <div class="brand" style="top:52px">
      <span class="brand__mark" style="width:14px;height:14px"></span>
      <div class="brand__name">Tolvane Handyman Services</div>
      <div class="brand__tag">Painting &amp; Remodeling</div>
    </div>
    <p class="tagline">FIX IT.<br>REPAIR IT.<br>CHANGE IT.<br>BUILD IT.</p>
    <div class="contact-tab">CONTACT US</div>
    <address class="contact">
      <div class="contact__company">Tolvane Handyman Service</div>
      <div class="contact__owner">Owner Owen Marsh</div>
      <div class="contact__line">(207) 555-0148</div>
      <div class="contact__line">owen@tolvanehandyman.com</div>
      <div class="contact__line">www.tolvanehandyman.com</div>
      <div class="contact__line">48 Birchwood Lane Kennebunk, Maine 04043</div>
    </address>
    <div class="social"><span></span><span></span><span></span><span></span></div>
    <div class="web-box">www.tolvanehandyman.com</div>
  </div>

  <div class="panel" style="left:437px;width:218px">
    <div class="brand brand--light" style="top:26px">
      <span class="brand__mark" style="width:22px;height:22px;margin-bottom:10px"></span>
      <div class="brand__name">Tolvane Handyman Services</div>
      <div class="brand__tag">Painting &amp; Remodeling</div>
    </div>
    <div class="photo" role="img" aria-label="Raised deck with stained wood posts and railings" style="left:0;top:125px;width:218px;height:287px;background:linear-gradient(180deg,#ffffff 0%,#c9cbd2 18%,#b98650 45%,#8e6038 70%,#9a958d 100%)"></div>
    <div style="position:absolute;left:0;top:412px;width:218px;height:13px;background:var(--blue)"></div>
    <p class="solution">WE ARE THE SOLUTION<br>TO YOUR PROBLEMS!</p>
    <div class="web-bar web-bar--right" style="top:488px"><svg viewBox="0 0 10 10"><circle cx="5" cy="5" r="4" fill="none" stroke="#fff"/><path d="M1 5h8M5 1v8" stroke="#fff" stroke-width=".8"/></svg>www.tolvanehandyman.com</div>
  </div>
</section>

<!-- Inside of brochure -->
<section class="sheet sheet--inside">

  <div class="panel" style="left:0;width:219px">
    <div class="photo" role="img" aria-label="Staircase during tread installation" style="left:0;top:0;width:219px;height:176px;background:linear-gradient(150deg,#d9d4cc 0%,#b9aa98 40%,#5a4535 70%,#cfc8bd 100%)"></div>
    <div class="side-bar"></div>
    <h2 class="section-title services__title">OUR SERVICES</h2>
    <p class="services__text">At Tolvane Handyman Services we are committed to client satisfaction and understanding that customer service is the foundation of our business. We are dedicated to providing our clients with quality workmanship performed in a prompt, professional manner. Our reliable team, second to none, will arrive neat in appearance and ready to work. Our technicians will treat each job, large or small, with the same care we would if we were repairing our own home.</p>
  </div>

  <div class="panel dark" style="left:219px;width:217px;height:330px">
    <div class="service" style="left:15px;top:24px;width:198px">
      <div class="service__head"><span class="service__rule" style="width:198px"></span><span class="service__tab">Interior Painting</span></div>
      <ul class="service__list">
        <li>Commercial &amp; Residential</li><li>Kitchen Cabinets</li><li>Painting</li><li>Walls trim &amp; doors</li><li>Celling repair</li><li>Staining &amp; polying trim</li>
      </ul>
    </div>
    <div class="service" style="left:15px;top:179px;width:198px">
      <div class="service__head"><span class="service__rule" style="width:198px"></span><span class="service__tab">Exterior Painting</span></div>
      <ul class="service__list">
        <li>Commercial &amp; Residential</li><li>New Painting &amp; Updates</li><li>All types of Siding</li><li>Power washing</li><li>Painting &amp; Staining of decks</li><li>Fence cleaning painting &amp; sealing</li><li>Furniture cleaning, painting &amp; sealing</li>
      </ul>
    </div>
  </div>

  <div class="photo" role="img" aria-label="Living room prepared for floor work with plastic-covered windows and a ladder" style="left:15px;top:330px;width:421px;height:179px;background:linear-gradient(100deg,#7d6e60 0%,#c6bfb4 30%,#a2968a 55%,#d6cfc4 80%,#8a7c6e 100%)"></div>

  <div class="panel" style="left:436px;width:219px">
    <div class="service" style="left:7px;top:24px;width:198px">
      <div class="service__head"><span class="service__rule" style="width:198px"></span><span class="service__tab" style="width:132px">Carpentry</span></div>
      <ul class="service__list">
        <li>Commercial &amp; Residential</li><li>Kitchen remodeling</li><li>Marble &amp; Granite countertops</li><li>Bathroom remodeling</li><li>Basement remodeling</li><li class="tight">Disabled accessible ramps &amp; bathroom installation</li><li>Room additions</li><li>All types of siding</li><li>Cabinetry</li><li>Sheet rocking</li>
      </ul>
    </div>
    <div class="photo" role="img" aria-label="Kitchen with newly painted dark cabinets" style="left:7px;top:191px;width:212px;height:138px;background:linear-gradient(180deg,#e4e2dd 0%,#4a5058 35%,#3b4048 60%,#d9d5cd 100%)"></div>
    <div class="service" style="left:7px;top:345px;width:190px">
      <div class="service__head"><span class="service__rule" style="width:190px"></span><span class="service__tab">Maintenance</span></div>
      <ul class="service__list">
        <li>Commercial &amp; Residential</li><li>Hanging Curtin's &amp; Blinds</li><li>Shelving</li><li>Lighting</li><li>Picture hanging</li><li>TV mounting</li><li>Desk &amp; furniture assembly</li><li>Fixture installation &amp; repair</li>
      </ul>
    </div>
    <div class="web-bar web-bar--right" style="top:487px;width:168px"><svg viewBox="0 0 10 10"><circle cx="5" cy="5" r="4" fill="none" stroke="#fff"/><path d="M1 5h8M5 1v8" stroke="#fff" stroke-width=".8"/></svg>www.tolvanehandyman.com</div>
  </div>
</section>

</body>
</html>
```